Brightstone Roofing Business Card

This is my current business card. But I’d like to make some changes. Somewhere on the card I’d like to list some of the services we offer. Maybe on the back? But I’d still like to keep the red. White and black modern look.

-residential & commercial roofing
-Roof Repairs & Maintenance
-Storm Damage & Insurance Claims specialist
-Christmas Lights and permanent Christmas lights
Fencing. Windows. Gutters. Siding. Sheetrock, painting.

```html
<!DOCTYPE html>
<html lang="en">
<head>
<meta charset="utf-8">
<title>Brightstone Roofing Business Card</title>
<link rel="stylesheet" href="https://fonts.googleapis.com/css2?family=Montserrat:wght@500;600;800&family=Audiowide&family=Open+Sans:wght@400;600&display=swap">
<style>
  :root {
    --stage: #d4d5d7;
    --card-black: #0b0b0b;
    --brand-red: #e1201f;
    --deep-red: #7a1010;
    --white: #ffffff;
    --soft-white: #f1f1f1;
  }
  * { box-sizing: border-box; margin: 0; padding: 0; }
  html, body {
    width: 1200px; height: 1200px; overflow: hidden;
    background: var(--stage);
  }
  .stage { position: relative; width: 1200px; height: 1200px; }
  .card {
    position: absolute; left: 162px; width: 876px; height: 502px;
    border-radius: 18px; overflow: hidden; background: var(--card-black);
    color: var(--white);
  }
  .card-front { top: 46px; }
  .card-back { top: 600px; }

  .tartan-band {
    position: absolute; left: 0; top: 0; width: 100%; height: 278px;
    background: linear-gradient(180deg, var(--deep-red) 0%, var(--brand-red) 28%, var(--brand-red) 62%, #2a0505 82%, #111 100%);
  }
  .band-rule {
    position: absolute; left: 0; top: 278px; width: 100%; height: 5px; background: var(--white);
  }
  .brand-seal {
    position: absolute; left: 336px; top: 92px; width: 204px; height: 204px;
    border-radius: 50%; background: var(--card-black); border: 8px solid var(--white);
    display: flex; align-items: center; justify-content: center; text-align: center;
    font-family: "Montserrat", sans-serif; font-weight: 800; font-size: 21px; line-height: 1.2;
    color: var(--white); letter-spacing: 0.5px;
  }

  .service-list {
    position: absolute; list-style: none;
    font-family: "Montserrat", sans-serif; font-weight: 500; font-size: 20px; line-height: 25px;
  }
  .service-list li { position: relative; padding-left: 0; margin-bottom: 11px; }
  .service-list li::before {
    content: ""; position: absolute; left: -18px; top: 10px;
    width: 7px; height: 7px; border-radius: 50%; background: var(--white);
  }
  .services-left { left: 38px; top: 316px; }
  .services-right { left: 532px; top: 314px; }

  .back-seal {
    position: absolute; left: 368px; top: 64px; width: 140px; height: 140px;
    border-radius: 50%; background: var(--brand-red); border: 7px solid var(--white);
  }
  .wordmark {
    position: absolute; left: 0; top: 218px; width: 100%; text-align: center;
    font-family: "Montserrat", sans-serif; font-weight: 800; font-size: 36px; line-height: 44px;
    color: var(--white); letter-spacing: 1px; text-transform: uppercase;
  }

  .holder { position: absolute; right: 470px; top: 362px; text-align: right; }
  .holder-name {
    font-family: "Audiowide", sans-serif; font-size: 34px; line-height: 40px; letter-spacing: 1px;
  }
  .holder-name .first { color: var(--brand-red); }
  .holder-role {
    font-family: "Open Sans", sans-serif; font-size: 20px; margin-top: 4px; color: var(--soft-white);
  }
  .holder-role .state { color: var(--brand-red); }
  .divider {
    position: absolute; left: 438px; top: 350px; width: 2px; height: 96px; background: #cfcfcf;
  }
  .contact-list {
    position: absolute; left: 462px; top: 350px; list-style: none;
    font-family: "Open Sans", sans-serif; font-size: 20px; color: var(--soft-white);
  }
  .contact-list li { display: flex; align-items: center; height: 34px; }
  .contact-list .phone { letter-spacing: 2px; }
  .contact-list svg { width: 18px; height: 18px; margin-right: 6px; fill: var(--brand-red); flex: none; }
  .tartan-strip {
    position: absolute; left: 0; bottom: 0; width: 100%; height: 18px;
    background: linear-gradient(180deg, var(--brand-red), var(--deep-red));
  }
</style>
</head>
<body>
<main class="stage">
  <section class="card card-front">
    <div class="tartan-band" role="img" aria-label="Red, white and black tartan pattern band"></div>
    <div class="band-rule"></div>
    <div class="brand-seal">Brightstone<br>Roofing Co.</div>
    <ul class="service-list services-left">
      <li>Residential<br>&amp; Commercial Roofing</li>
      <li>Roof Repairs &amp; Maintenance</li>
      <li>Storm Damage &amp;<br>Insurance Claims specialist</li>
    </ul>
    <ul class="service-list services-right">
      <li>Christmas Lights &amp;<br>permanent Christmas lights</li>
      <li>Fencing</li>
      <li>Windows, Gutters &amp; Siding</li>
      <li>Sheetrock &amp; painting</li>
    </ul>
  </section>

  <section class="card card-back">
    <div class="back-seal"></div>
    <div class="wordmark">Brightstone<br>Roofing Co.</div>
    <div class="holder">
      <div class="holder-name"><span class="first">GRANT</span> MERCER</div>
      <div class="holder-role">Roofing contractor in <span class="state">Texas</span></div>
    </div>
    <div class="divider"></div>
    <ul class="contact-list">
      <li class="phone">
        <svg viewBox="0 0 24 24"><path d="M6.6 10.8a15.1 15.1 0 0 0 6.6 6.6l2.2-2.2c.3-.3.7-.4 1-.2 1.1.4 2.3.6 3.6.6.6 0 1 .4 1 1V20c0 .6-.4 1-1 1A17 17 0 0 1 3 4c0-.6.4-1 1-1h3.5c.6 0 1 .4 1 1 0 1.3.2 2.5.6 3.6.1.3 0 .7-.2 1z"/></svg>
        682-555-0148
      </li>
      <li>
        <svg viewBox="0 0 24 24"><path d="M2 5h20v14H2z" fill="none"/><path d="M2 5h20v2l-10 6L2 7zM2 9l10 6 10-6v10H2z"/></svg>
        Grant@brightstoneroofing.co
      </li>
      <li>
        <svg viewBox="0 0 24 24"><path d="M12 2a10 10 0 1 0 0 20 10 10 0 0 0 0-20zm6.9 6h-3a15.6 15.6 0 0 0-1.4-3.6A8 8 0 0 1 18.9 8zM12 4c.8 1.2 1.5 2.5 1.9 4h-3.8c.4-1.5 1.1-2.8 1.9-4zM4.3 14a8 8 0 0 1 0-4h3.4a16.5 16.5 0 0 0 0 4zm.8 2h3a15.6 15.6 0 0 0 1.4 3.6A8 8 0 0 1 5.1 16zm3-8h-3a8 8 0 0 1 4.4-3.6C8.9 5.5 8.4 6.7 8.1 8zM12 20c-.8-1.2-1.5-2.5-1.9-4h3.8c-.4 1.5-1.1 2.8-1.9 4zm2.3-6H9.7a14.7 14.7 0 0 1 0-4h4.6a14.7 14.7 0 0 1 0 4zm.2 5.6c.6-1.1 1.1-2.3 1.4-3.6h3a8 8 0 0 1-4.4 3.6zm1.8-5.6a16.5 16.5 0 0 0 0-4h3.4a8 8 0 0 1 0 4z"/></svg>
        www.brightstoneroofing.co
      </li>
    </ul>
    <div class="tartan-strip" role="img" aria-label="Thin red, white and black tartan pattern strip"></div>
  </section>
</main>
</body>
</html>
```